Website design improvement for existing site

We would like design ideas for how the inner pages (not the homepage) of www.talbrookpictures.com could be improved. We don't want to totally redesign the website. We want to improve / enhance / develop it further to look high-end, sophisticated and visually stunning.

Target Market(s)

High end video production clients. National and international TV networks and brands wanting commercial filming.

Industry/Entity Type

Videography

Other font styles liked:
• Existing site fonts

Requirements
Must have
• Improvement on the existing inner pages without totally re-working the design. We want to achieve a high-end sophisticated look with the existing branding (colours, images etc)
Nice to have
• Any ideas for improving the homepage are also welcome but we are mostly happy with this page so it is not the priority.
Should not have
• Any major changes to colours, styles etc.

```html
<!DOCTYPE html>
<html lang="en">
<head>
<meta charset="utf-8">
<title>Talbrook Pictures – Contact</title>
<link href="https://fonts.googleapis.com/css2?family=Open+Sans:wght@300;400;600;700;800&display=swap" rel="stylesheet">
<style>
:root{
  --red:#f21f22;
  --red-dark:#e01b1e;
  --ink:#222;
  --footer:#242424;
  --white:#fff;
  --muted:#bdbdbd;
  --band:#f2f2f2;
}
*{box-sizing:border-box;margin:0;padding:0}
html,body{width:966px;height:1200px;overflow:hidden}
body{font-family:"Open Sans",Arial,sans-serif;background:var(--white);position:relative;color:var(--ink)}
.abs{position:absolute}

/* hero */
.hero{left:0;top:0;width:966px;height:284px;background:radial-gradient(ellipse at 70% 45%,#8a8079 0%,#4c4642 45%,#1f1d1c 100%)}
.brand{left:200px;top:20px;display:flex;align-items:center;gap:9px;color:var(--white);font-weight:700;font-size:17px;letter-spacing:1px;line-height:1.1}
.brand-dot{width:34px;height:34px;border-radius:50%;background:var(--red)}
.nav{right:202px;top:29px;display:flex;gap:14px;list-style:none}
.nav li{color:var(--white);font-size:8.5px;font-weight:600;text-transform:uppercase}
.hero-copy{left:0;width:966px;top:122px;text-align:center}
.hero-copy .h1{color:var(--white);font-weight:800;font-size:30px;line-height:36px}
.hero-copy .h2{color:var(--white);font-weight:300;font-size:22px;line-height:26px}
.hero-copy .h3{color:var(--red);font-weight:800;font-size:21px;line-height:28px}

/* fun */
.fun-title{left:0;width:966px;top:306px;text-align:center;color:var(--red);font-weight:800;font-size:30px}
.clip{top:365px;width:276px;height:223px;background:var(--band)}
.clip-media{width:276px;height:186px;position:relative}
.clip-1 .clip-media{background:linear-gradient(135deg,#8a6a4c,#c4a58a 55%,#6e5640)}
.clip-2 .clip-media{background:linear-gradient(135deg,#3c3a38,#8a8682 50%,#1f1e1d)}
.play{position:absolute;left:115px;top:70px;width:44px;height:44px;border-radius:50%;background:var(--white)}
.play svg{position:absolute;left:15px;top:12px}
.clip-caption{text-align:center;color:var(--red);font-weight:600;font-size:14.5px;line-height:37px}

/* contact */
.contact-form{left:0;top:620px;width:483px;height:328px;background:var(--red)}
.contact-title{left:30px;top:30px;color:var(--white);font-weight:300;font-size:19.5px;text-transform:uppercase}
.contact-title b{font-weight:700}
.field{border:1px solid rgba(255,255,255,.9);color:var(--white);font-size:9px;padding:11px 12px}
.submit{left:30px;top:259px;width:421px;height:37px;background:var(--white);color:var(--red);font-weight:700;font-size:10px;text-align:center;line-height:37px;box-shadow:0 2px 4px rgba(0,0,0,.2)}
.map{left:483px;top:620px;width:483px;height:328px;background:linear-gradient(160deg,#ece9e3 0%,#e2e6de 50%,#d7e3d2 100%)}
.info-card{left:601px;top:690px;width:234px;height:187px;background:var(--white);box-shadow:0 2px 8px rgba(0,0,0,.2);text-align:center;font-size:9.5px;color:#333}
.info-card .lbl{color:var(--red);font-weight:700}

/* footer */
.footer{left:0;top:948px;width:966px;height:225px;background:var(--footer);color:var(--muted)}
.foot-brand{left:200px;top:48px;display:flex;align-items:center;gap:8px;color:var(--white);font-weight:700;font-size:15px;line-height:1.1;letter-spacing:1px}
.foot-brand .brand-dot{width:30px;height:30px}
.foot-about{left:200px;top:99px;width:160px;font-size:7px;line-height:14px}
.foot-h{color:var(--white);font-weight:700;font-size:11.5px;text-transform:uppercase}
.links{left:384px;top:88px;list-style:none;color:var(--white);font-size:7.5px}
.links li{height:21.6px}
.links li::before{content:"» ";font-size:8px}
.foot-contact{left:487px;top:84px;width:120px;color:var(--white);font-size:7px;line-height:14px}
.foot-contact p{padding:4px 0 6px;border-bottom:1px solid #3a3a3a}
.foot-contact p:last-child{border:0}
.news-input{left:636px;top:79px;width:101px;height:24px;background:#2f2f2f;color:#888;font-size:7px;line-height:24px;padding-left:11px}
.news-btn{left:737px;top:79px;width:29px;height:24px;background:var(--red)}
.social{top:146px;width:30px;height:30px;border-radius:50%}
.copyright{left:0;top:1173px;width:966px;height:27px;background:var(--red-dark);color:var(--white);font-size:7.5px;line-height:27px}
</style>
</head>
<body>

<header class="hero abs" role="img" aria-label="Dim close-up photo of a baker dusting a wooden board with flour"></header>
<div class="brand abs"><span class="brand-dot"></span><span>TALBROOK<br>PICTURES</span></div>
<ul class="nav abs">
  <li>Home</li><li>About</li><li>Process</li><li>Brand Stories</li><li>Contact</li>
</ul>
<div class="hero-copy abs">
  <div class="h1">LET'S TALK ABOUT</div>
  <div class="h2">YOUR PROJECT</div>
  <div class="h3">READY TO BEGIN?</div>
</div>

<h2 class="fun-title abs">AND JUST FOR FUN</h2>
<div class="clip clip-1 abs" style="left:200px">
  <div class="clip-media" role="img" aria-label="Video still of hands washing under a kitchen tap">
    <span class="play"><svg width="16" height="20" viewBox="0 0 16 20"><path d="M2 1 L15 10 L2 19Z" fill="#333"/></svg></span>
  </div>
  <div class="clip-caption">SinkCam clip from The Crumb</div>
</div>
<div class="clip clip-2 abs" style="left:490px">
  <div class="clip-media" role="img" aria-label="Video still of a camera rig filming pans on a kitchen stove">
    <span class="play"><svg width="16" height="20" viewBox="0 0 16 20"><path d="M2 1 L15 10 L2 19Z" fill="#333"/></svg></span>
  </div>
  <div class="clip-caption">Dough Heart clip from The Crumb</div>
</div>

<section class="contact-form abs">
  <h3 class="contact-title abs">Or complete the <b>contact</b> form below</h3>
  <div class="field abs" style="left:30px;top:72px;width:206px;height:35px">Name</div>
  <div class="field abs" style="left:244px;top:72px;width:207px;height:35px">Phone</div>
  <div class="field abs" style="left:30px;top:121px;width:421px;height:35px">Email</div>
  <div class="field abs" style="left:30px;top:170px;width:421px;height:72px">Messages</div>
  <div class="submit abs">SUBMIT</div>
</section>
<div class="map abs" role="img" aria-label="Street map around the studio location"></div>
<div class="info-card abs">
  <svg class="abs" style="left:110px;top:17px" width="14" height="20" viewBox="0 0 14 20"><path d="M7 0C3 0 0 3 0 7c0 5 7 13 7 13s7-8 7-13c0-4-3-7-7-7z" fill="#f21f22"/><circle cx="7" cy="7" r="2.6" fill="#fff"/></svg>
  <p class="abs" style="left:16px;top:42px;width:202px;line-height:16px">Located in Dunmere, North Riding, and available for UK-wide projects.</p>
  <svg class="abs" style="left:110px;top:87px" width="15" height="15" viewBox="0 0 24 24"><path d="M6.6 10.8c1.4 2.8 3.8 5.1 6.6 6.6l2.2-2.2c.3-.3.7-.4 1-.2 1.1.4 2.3.6 3.6.6.6 0 1 .4 1 1V20c0 .6-.4 1-1 1C10.6 21 3 13.4 3 4c0-.6.4-1 1-1h3.5c.6 0 1 .4 1 1 0 1.3.2 2.5.6 3.6.1.3 0 .7-.2 1z" fill="#f21f22"/></svg>
  <p class="abs" style="left:0;top:110px;width:234px"><span class="lbl">CALL US ON</span> 01632 960418</p>
  <svg class="abs" style="left:117px;top:140px" width="15" height="11" viewBox="0 0 15 11"><rect x=".5" y=".5" width="14" height="10" fill="none" stroke="#f21f22"/><path d="M.5.5 7.5 6.5 14.5.5" fill="none" stroke="#f21f22"/></svg>
  <p class="abs" style="left:0;top:156px;width:234px"><span class="lbl">EMAIL US AT</span> hello@talbrookpictures.com</p>
</div>

<footer class="footer abs">
  <div class="foot-brand abs"><span class="brand-dot"></span><span>TALBROOK<br>PICTURES</span></div>
  <p class="foot-about abs">Talbrook Pictures was set up by Cara Talbrook. The idea? To help businesses harness the narrative power of film to tell better brand stories. To allow companies to use a creative, visual medium to produce unique and beautiful narratives. Brand messages that truly engage with customers and better define who they are</p>
  <h4 class="foot-h abs" style="left:382px;top:51px">Quik Link</h4>
  <ul class="links abs">
    <li>HOME</li><li>ABOUT</li><li>PROCESS</li><li>BRAND STORIES</li><li>CONTACT</li>
  </ul>
  <h4 class="foot-h abs" style="left:486px;top:51px">Contact Us</h4>
  <div class="foot-contact abs">
    <p>Located in Dunmere, North Riding, and available for UK-wide projects.</p>
    <p>Call us on 01632 960418</p>
    <p>Email us at hello@talbrookpictures.com</p>
  </div>
  <h4 class="foot-h abs" style="left:636px;top:51px">Newsletters</h4>
  <div class="news-input abs">Your Email Address</div>
  <div class="news-btn abs"><svg class="abs" style="left:9px;top:6px" width="11" height="11" viewBox="0 0 11 11"><path d="M11 0 0 5l4 1.5L5 11z" fill="#fff"/></svg></div>
  <h4 class="foot-h abs" style="left:639px;top:115px">Stay Connected</h4>
  <span class="social abs" style="left:636px;background:#e52d27"></span>
  <span class="social abs" style="left:669px;background:#3b5998"></span>
  <span class="social abs" style="left:702px;background:#3fa9e6"></span>
  <span class="social abs" style="left:736px;background:#dd4b39"></span>
</footer>
<div class="copyright abs">
  <span class="abs" style="left:201px">Copyright © 2017 <b>Talbrook Pictures</b>. All Rights</span>
  <span class="abs" style="right:200px">Design &amp; Developed by <b>BRIGHTLINE STUDIO</b></span>
</div>

</body>
</html>
```